New look and feel for investment website

Hi

Our website needs a crisp and professional look and feel applying to it. Here’s the address: http://www.brightplinth.co.uk. Since posting the brief yesterday (Tuesday, 16 August), we've reduced the amount of content on the home page, which should make life a little easier for you. We will come back later today, with some points of reference in terms of sites we like the look of. (See below)

17 August, 1.20pm GMT. OK, comments generally on the designs submitted so far. Please keep in mind that images of graphs, piles of coins, paper money and pretty females are not what is required. Better to think in terms of abstract imagery instead. Ratios? Circles? Relationships? Patterns? Not money,sex,graphs etc. Hope that helps.

For guidance on look and feel, please refer to these sites, which we like:

http://www.morvelle.co.uk/
http://www.qz.com/
https://www.harrowfieldtamsin.com
https://www.pirelconcerns.com
https://www.kvantule.com
Updates

Here's the Tall Beacons logo created in AI CS5.

Our market is professional financial advisers and relatively sophisticated private investors. The look and feel therefore should be slick and sophisticated - not 'lively' and lightweight, more like a banking site. Please read the brief again where we've added a list of websites that we really like the look of to get a better feel for what we're looking for. Thanks once again, we appreciate the work you're putting in.

It's essential that all the elements that are on the current home page be included on all new designs. 

We use a device in our e-mails which you may wish to incorporate in your design.

Target Market(s)

Professional financial advisers. People who know about investment and money.

Industry/Entity Type

Investment

Requirements
Should not have
• Graphs or people.

```html
<!DOCTYPE html>
<html lang="en">
<head>
<meta charset="utf-8">
<title>Tall Beacons – Value investing</title>
<link href="https://fonts.googleapis.com/css2?family=Bebas+Neue&family=Oswald:wght@600&family=PT+Sans:ital,wght@0,400;0,700;1,400;1,700&family=Open+Sans:wght@400;600&display=swap" rel="stylesheet">
<style>
:root{
  --orange:#f9a93a;
  --orange-dark:#f29a1f;
  --red:#e8222a;
  --blue:#1e9be0;
  --blue-soft:#3a8fd6;
  --sky:#a9d2ee;
  --panel-blue:#dfeaf4;
  --beige:#f3efe6;
  --beige-strip:#e9e3d3;
  --page:#eff4f8;
  --ink:#5c5c5c;
  --ink-dark:#333;
  --grey:#c9c9c9;
  --white:#fff;
}
*{box-sizing:border-box;margin:0;padding:0}
html,body{width:1103px;height:1200px;overflow:hidden}
body{position:relative;background:var(--white);font-family:"PT Sans",Arial,sans-serif;color:var(--ink)}
a{color:inherit;text-decoration:none}

.brand{position:absolute;left:139px;top:48px;display:flex;align-items:center;gap:8px;font-family:"Open Sans",Arial,sans-serif;font-weight:600;font-size:30px;color:#9a9a9a;letter-spacing:-.5px}
.brand-dot{width:9px;height:9px;background:var(--orange-dark)}

.main-nav{position:absolute;left:325px;top:3px;width:646px;height:97px;background:var(--orange)}
.main-nav a{position:absolute;font-size:11.5px;color:var(--ink-dark);white-space:nowrap}
.main-nav .current{background:#fde3b4;padding:2px 7px;margin-left:-7px;margin-top:-2px}
.nav-rule{position:absolute;top:12px;height:72px;border-left:1px dotted #b06d10}
.util-bar{position:absolute;left:325px;top:100px;width:646px;height:29px;background:var(--red);display:flex;justify-content:flex-end;align-items:center;padding-right:8px;font-size:11.5px;font-weight:700;color:var(--white)}
.util-bar a+a::before{content:"|";margin:0 6px}

.hero{position:absolute;left:0;top:129px;width:1103px;height:220px;background:linear-gradient(100deg,#cfe5f6 0%,#9dc9ec 35%,#d9ecf9 70%,#b6d6f0 100%);border-top:1px dotted #8aa}
.hero-art{position:absolute;left:140px;top:-18px;width:260px;height:220px;background:linear-gradient(135deg,#2bb6a6,#f7a533 55%,#e8322c);border-radius:40% 10% 30% 50%;opacity:.85}
.hero-quote{position:absolute;left:474px;top:50px;width:480px;font-family:"Oswald","Arial Narrow",sans-serif;font-weight:600;font-size:28px;line-height:29px;color:#2f2f2f}
.qmark{color:var(--red);font-size:40px;position:absolute}
.qmark.open{left:-22px;top:-6px}
.qmark.close{position:relative;top:10px;margin-left:4px}

.content{position:absolute;left:0;top:349px;width:1103px;height:695px;background:var(--page)}
.intro{position:absolute;left:143px;top:16px;width:546px}
.intro h1{font-family:"Bebas Neue",Impact,sans-serif;font-weight:400;font-size:33px;color:var(--blue);line-height:1}
.intro h2{margin-top:7px;font-weight:400;font-size:19px;line-height:21px;color:var(--blue-soft)}
.intro p{font-size:11.3px;line-height:14px;margin-top:10px;text-align:justify}
.intro h2+p{margin-top:14px}
.callout{list-style:none;margin-top:10px}
.callout li{position:relative;padding-left:19px;font-size:17.5px;line-height:20px;color:#666;margin-top:8px}
.callout li::before{content:"";position:absolute;left:2px;top:5px;border:5px solid transparent;border-left:7px solid var(--orange-dark);border-right:0}
.cta{position:absolute;left:140px;top:582px;width:484px;height:36px;background:var(--orange);border-radius:4px;padding:8px 13px;font-style:italic;font-size:18px;color:var(--white)}
.cta a{font-weight:700;text-decoration:underline}

.divider{position:absolute;left:700px;top:24px;height:640px;border-left:1px dashed var(--orange-dark)}
.divider::after{content:"";position:absolute;left:-4px;bottom:-6px;width:7px;height:7px;border-radius:50%;background:var(--orange-dark)}

.panel-head{height:36px;padding:8px 0 0 54px;font-size:16px;position:relative}
.panel-head::after{content:"";position:absolute;right:0;top:0;border:5px solid transparent;border-top-color:var(--blue-soft);border-right-color:var(--blue-soft)}
.register{position:absolute;left:711px;top:18px;width:260px;height:173px;background:var(--panel-blue);border-bottom:3px solid #b9cfe0}
.register .panel-head{background:var(--sky);color:#333}
.register .panel-body{padding:8px 10px 0 40px;font-size:11.3px;line-height:14px;color:#333;text-align:justify}
.register .trial{color:var(--red)}
.register .panel-body a{color:#8a5a14;text-decoration:underline}
.btn-register{position:absolute;left:54px;top:130px;width:178px;height:33px;background:var(--red);color:var(--white);font-family:"Oswald",sans-serif;font-weight:600;font-size:16px;padding:5px 0 0 16px;border:1px solid #a31015}
.btn-register span{position:absolute;right:0;top:0;width:36px;height:31px;background:#c4161c;display:flex;align-items:center;justify-content:center}

.benefits{position:absolute;left:711px;top:198px;width:260px;height:420px;background:linear-gradient(90deg,var(--beige-strip) 0 32px,var(--beige) 32px);border-bottom:3px solid #ddd5c2}
.benefits .panel-head{background:var(--orange);color:#333}
.benefits .panel-head::after{border-top-color:#b36a0e;border-right-color:#b36a0e}
.benefits ul{list-style:none;padding:18px 10px 0 38px;display:flex;flex-direction:column;gap:15px}
.benefits li{position:relative;font-size:11.3px;line-height:14px;color:#333}
.benefits li::before{content:"···›";position:absolute;left:-34px;top:-3px;color:#888;letter-spacing:1px}
.benefits li.spaced{margin-top:14px}
.read-more{position:absolute;left:899px;top:634px;width:69px;height:15px;background:var(--orange);color:var(--white);font-style:italic;font-weight:700;font-size:10px;padding:1px 0 0 5px;clip-path:polygon(0 0,90% 0,100% 50%,90% 100%,0 100%)}

.site-footer{position:absolute;left:0;top:1044px;width:1103px;height:120px;background:var(--grey)}
.footer-nav{position:absolute;left:143px;top:21px;width:720px;font-size:11.3px;line-height:15px;color:#333}
.footer-contact{position:absolute;left:143px;top:79px;font-size:11.3px;line-height:15px;color:#222}
.footer-brand{position:absolute;right:110px;top:95px;font-family:"Open Sans",sans-serif;font-weight:600;font-size:17px;color:#8e8e8e}
.legal-bar{position:absolute;left:0;top:1164px;width:1103px;height:36px;background:var(--orange);padding:11px 0 0 143px;font-size:11px;color:#333}
.legal-bar a{font-style:italic;font-weight:700;text-decoration:underline}
.social{position:absolute;right:137px;top:9px;display:flex;gap:3px}
.social span{width:18px;height:18px;background:#222;border-radius:3px}
</style>
</head>
<body>

<div class="brand"><span>Tall Beacons</span><span class="brand-dot"></span></div>

<nav class="main-nav">
  <span class="nav-rule" style="left:137px"></span>
  <span class="nav-rule" style="left:347px"></span>
  <span class="nav-rule" style="left:568px"></span>
  <a class="current" style="left:20px;top:17px">Home</a>
  <a style="left:20px;top:44px">Two Minute Guide</a>
  <a style="left:20px;top:70px">About our analyses</a>
  <a style="left:155px;top:17px">Current &amp; year to date performance</a>
  <a style="left:155px;top:44px">Watch list</a>
  <a style="left:155px;top:70px">Other key numbers</a>
  <a style="left:366px;top:17px">About value investing</a>
  <a style="left:366px;top:44px">Back tested results</a>
  <a style="left:366px;top:70px">The Broadline 1000 and the Summit 500 index</a>
  <a style="left:586px;top:17px">FAQs</a>
</nav>
<div class="util-bar"><a>Login</a><a>Register for free</a><a>Contact us</a><a>Terms &amp; Conditions</a></div>

<section class="hero">
  <div class="hero-art" role="img" aria-label="Abstract rising ribbons and arrows in teal, orange and red"></div>
  <blockquote class="hero-quote"><span class="qmark open">“</span>A potential return of 23.57 % a year from America’s biggest businesses with the emphasis firmly on capital preservation.<span class="qmark close">”</span></blockquote>
</section>

<main class="content">
  <article class="intro">
    <h1>Introduction</h1>
    <h2>A methodical and consistent software-driven process for identifying and investing in, undervalued stocks</h2>
    <p>The attractions of value investing need no explanation to those who subscribe to the concept. But it's impractical, if not impossible, for the private investor to implement the strategy (using direct holdings as distinct to collective funds) consistently. Although the data may be available, to undertake fundamental analysis regularly, on a reasonable number of stocks, entails a significant amount of time and effort.</p>
    <p>By definition - and depending on where you look and market conditions - undervalued businesses (stocks) are relatively scarce. So where does the value investor begin their search? Which and how many businesses must be scrutinised before one undervalued entity is found? And having identified a stock that's trading at less than its fair value, will that be the case next week or next month? Fundamentals can change for the worse at any time, so without the benefit of regular analysis, how will the value investor</p>
    <ul class="callout">
      <li>Those problems - and others - have now been solved.</li>
      <li>Our software produces the quantitative analysis value investors need.</li>
    </ul>
    <p>Once a month, month in month out, our program scrutinises the key fundamentals of 1,000 large cap American companies which between them account for 92% of the US securities market.</p>
    <p>First of all, the program sifts through each of the 1,000 stocks searching for favourable arrays of fundamentals: that process usually filters out between 950 and 975 stocks. The software then applies a range of algorithms to the short-listed stocks to identify any which are trading at 35% (or more) below their estimated fair value. There are times when not one single stock on the shortlist meets our criteria. But when they do - and if there's room - those stocks are added to our portfolio.</p>
    <ul class="callout">
      <li>We're not stock pickers, share tippers or brokers.<br>What we do is analyse stocks and show you which of them our software flags as being undervalued.</li>
    </ul>
  </article>
  <div class="cta">For more details and the results to date...<a>please go here</a></div>

  <span class="divider"></span>

  <aside class="register">
    <div class="panel-head">Free Registration</div>
    <div class="panel-body"><span class="trial">Free trial period:</span><br>if you would like to monitor the portfolio's performance for six months free of charge then please <a>complete the registration form</a>.</div>
    <a class="btn-register">Register Me Free<span><svg width="12" height="14" viewBox="0 0 12 14"><path d="M2 1l8 6-8 6" fill="none" stroke="#fff" stroke-width="3"/></svg></span></a>
  </aside>

  <aside class="benefits">
    <div class="panel-head">Benefits &amp; Features</div>
    <ul>
      <li>Average, annualised compound return over to : 23.57 %</li>
      <li>So far this year, the portfolio's return is 13.49 %:</li>
      <li>Worst ever annual loss: -1.48 %; best ever annual gain: 69.77 %</li>
      <li>Average return per trade including losing trades: 24.44 %</li>
      <li>Maximum number of winning/losing trades in a row: 11/4.</li>
      <li>Average number of days a stock stays in the portfolio: 287</li>
      <li>An average of five trades a year and never more than five holdings at any one time.</li>
      <li class="spaced">86 trades in total, of which<br>65 were profitable - a success rate<br>of 75.58 %</li>
    </ul>
  </aside>
  <a class="read-more">Read more...</a>
</main>

<footer class="site-footer">
  <div class="footer-nav">Navigate here:<br>Home / Two minute guide / Current &amp; year to date performance / Watch list / Other key numbers / Back tested results / History of all trades / About our analyses / About value investing / The Broadline 1000 and the Summit 500 index / FAQs</div>
  <div class="footer-contact">Do you have any Questions?<br>Please feel free to e-mail us at: info@tallbeacons.co.uk.</div>
  <div class="footer-brand">Tall Beacons</div>
</footer>
<div class="legal-bar">© Tall Beacons Ltd 2011. All rights reserved. Use of this website constitutes acceptance of our <a>User Agreement and Privacy Policy</a>.
  <div class="social"><span></span><span></span><span></span><span></span></div>
</div>

</body>
</html>
```